Business Card Design & Logo Design

Im a new company selling: balloons, bespoke gift wrapping services & Christmas decorating services i.e. I will come and decorate your tree, wrap your xmas presents, set & decorate your dining table, help you host your xmas party etc. etc.

I don't do 'cheesey' stuff so need a sophisticated card.

I love b&w colours, I love stripes and smart looking stuff.

I do already have an idea and if I don't find anything else then I will go with my idea but would then just need somebody to create the artwork for me.

www.lanternpeak.co.uk is currently in the process of being designed so any ideas of logos/designs must also work with a website.

Business

Contact Information for Business Card

Lantern Peak
Elmford upon Lea
KD52 8RT
Northfoldshire
01632 960418
or
07700 900631

hello@lanternpeak.co.uk

```html
<!DOCTYPE html>
<html lang="en">
<head>
<meta charset="utf-8">
<title>Lantern Peak — Logo &amp; Business Card</title>
<link rel="stylesheet" href="https://fonts.googleapis.com/css2?family=Open+Sans:wght@400;600&display=swap">
<style>
  :root {
    --brand-pink: #ec1f78;
    --ink: #111111;
    --paper: #ffffff;
    --front-base: #272626;
    --front-stripe-light: #b1afaf;
    --front-stripe-mid: #565251;
    --front-foot: #000000;
    --back-base: #a9a8a7;
    --back-stripe-soft: #bdbcbb;
    --back-stripe-pale: #dddcdc;
    --icon-grey: #a9a19b;
    --icon-fill-dark: #8f8f8f;
    --icon-fill-light: #d3ceca;
  }
  * { box-sizing: border-box; margin: 0; padding: 0; }
  html, body { width: 1200px; height: 1000px; overflow: hidden; background: var(--paper); }
  body { position: relative; font-family: "Open Sans", Arial, sans-serif; }

  .brand-mark {
    position: absolute; left: 0; top: 118px; width: 1200px;
    text-align: center; color: var(--brand-pink);
    font-family: "Open Sans", Arial, sans-serif; font-weight: 600;
    font-size: 104px; line-height: 1; letter-spacing: 1px;
  }

  .card {
    position: absolute; top: 347px; width: 345px; height: 521px;
    border: 1px solid var(--ink); overflow: hidden; background: var(--paper);
  }
  .card--front { left: 200px; }
  .card--back { left: 630px; }

  .stripes { position: absolute; left: 0; top: 0; width: 100%; }
  .card--front .stripes { height: 265px; background: var(--front-base); }
  .card--back .stripes { height: 393px; background: var(--back-base); }
  .stripe { position: absolute; top: 0; bottom: 0; width: 21px; }
  .stripe--light { background: var(--front-stripe-light); }
  .stripe--mid { background: var(--front-stripe-mid); }
  .stripe--soft { background: var(--back-stripe-soft); }
  .stripe--pale { background: var(--back-stripe-pale); }

  .name-band { position: absolute; left: 0; top: 265px; width: 100%; height: 111px; background: var(--paper); }
  .name-band__title {
    position: absolute; left: 0; top: 22px; width: 100%; text-align: center;
    color: var(--brand-pink); font-weight: 600; font-size: 32px; line-height: 1;
  }
  .name-band__rule { position: absolute; left: 0; top: 73px; width: 100%; height: 4px; background: var(--ink); }

  .services { position: absolute; left: 0; width: 100%; }
  .card--front .services { top: 376px; height: 145px; background: var(--front-foot); }
  .card--back .services { top: 393px; height: 128px; background: var(--paper); }
  .service { position: absolute; width: 90px; margin-left: -45px; text-align: center; }
  .card--front .service { top: 28px; }
  .card--back .service { top: 12px; }
  .service__icon { display: block; width: 40px; height: 66px; margin: 0 auto; border-radius: 4px; }
  .card--front .service__icon { background: var(--icon-fill-dark); }
  .card--back .service__icon { background: var(--icon-fill-light); }
  .service__label { display: block; margin-top: 6px; font-size: 10px; letter-spacing: 0.2px; }
  .card--front .service__label { color: var(--paper); }
  .card--back .service__label { color: var(--icon-grey); }

  .contact {
    position: absolute; left: 0; top: 92px; width: 100%;
    text-align: center; color: var(--ink);
  }
  .contact__address { font-size: 21px; line-height: 28px; }
  .contact__phones { margin-top: 30px; font-size: 22px; line-height: 29px; letter-spacing: 0.5px; }
  .contact__email { margin-top: 34px; font-size: 15px; line-height: 20px; }
  .contact__web { margin-top: 6px; font-size: 18px; line-height: 22px; }
</style>
</head>
<body>
  <h1 class="brand-mark">Lantern Peak</h1>

  <section class="card card--front" aria-label="Business card front">
    <div class="stripes">
      <span class="stripe stripe--light" style="left:28px"></span>
      <span class="stripe stripe--mid" style="left:73px"></span>
      <span class="stripe stripe--light" style="left:118px"></span>
      <span class="stripe stripe--mid" style="left:164px"></span>
      <span class="stripe stripe--light" style="left:209px"></span>
      <span class="stripe stripe--mid" style="left:255px"></span>
      <span class="stripe stripe--light" style="left:300px"></span>
    </div>
    <div class="name-band">
      <p class="name-band__title">Lantern Peak</p>
      <div class="name-band__rule"></div>
    </div>
    <div class="services">
      <div class="service" style="left:85px">
        <span class="service__icon" role="img" aria-label="Ornate Christmas tree icon"></span>
        <span class="service__label">CHRISTMAS</span>
      </div>
      <div class="service" style="left:170px">
        <span class="service__icon" role="img" aria-label="Patterned balloon icon"></span>
        <span class="service__label">BALLOONS</span>
      </div>
      <div class="service" style="left:262px">
        <span class="service__icon" role="img" aria-label="Wrapped gift box icon"></span>
        <span class="service__label">GIFTWRAP</span>
      </div>
    </div>
  </section>

  <section class="card card--back" aria-label="Business card back">
    <div class="stripes">
      <span class="stripe stripe--pale" style="left:28px"></span>
      <span class="stripe stripe--soft" style="left:73px"></span>
      <span class="stripe stripe--pale" style="left:118px"></span>
      <span class="stripe stripe--soft" style="left:164px"></span>
      <span class="stripe stripe--pale" style="left:209px"></span>
      <span class="stripe stripe--soft" style="left:255px"></span>
      <span class="stripe stripe--pale" style="left:300px"></span>
    </div>
    <div class="contact">
      <p class="contact__address">Elmford upon Lea<br>KD52 8RT Northfoldshire</p>
      <p class="contact__phones">01632 960418<br>07700 900631</p>
      <p class="contact__email">hello@lanternpeak.co.uk</p>
      <p class="contact__web">www.lanternpeak.co.uk</p>
    </div>
    <div class="services">
      <div class="service" style="left:85px">
        <span class="service__icon" role="img" aria-label="Ornate Christmas tree icon"></span>
        <span class="service__label">CHRISTMAS</span>
      </div>
      <div class="service" style="left:170px">
        <span class="service__icon" role="img" aria-label="Patterned balloon icon"></span>
        <span class="service__label">BALLOONS</span>
      </div>
      <div class="service" style="left:260px">
        <span class="service__icon" role="img" aria-label="Wrapped gift box icon"></span>
        <span class="service__label">GIFTWRAP</span>
      </div>
    </div>
  </section>
</body>
</html>
```